We need a business card design for our residential home building company based out of East Tennessee and the Smoky Mountains. We have 30 years of experience, and we plan to build homes not only in the state of Tennessee, but out of state as well. We are a different kind of production home builder; we aim to build homes cost-effectively and efficiently but with the character, dignity, and charm of historic homes. Our homes have a timeless style with modern floorplans and features. We would like to see designs that embody a classic style with accents of gold, red, and blue. The resulting business card should convey elegance, strength, character, and trust as well as the careful balance of the old and new.
Motto: "Shaping Lasting Roots"
Reason: I would like to extend the deadline so that more changes can be made to the best designs.
Target Market(s)
Adults 40+ from the Northern states looking to settle in Tennessee.
Industry/Entity Type
Residential
Contact Information for Business Card
Birchwood Dwellworks, LLC
Marla Pettigrew | Director of Operations
20815 Thornbury Lane | Suite 300
Knoxville, TN 37091
Office: (865)413-2958
Mobile: (865)690-8142
Email: marla@birchwooddwellworks.example

```html
<!DOCTYPE html>
<html lang="en">
<head>
<meta charset="utf-8">
<title>Birchwood Dwellworks, LLC — Business Card</title>
<link href="https://fonts.googleapis.com/css2?family=Cagliostro&display=swap" rel="stylesheet">
<style>
  :root {
    --page: #ffffff;
    --card: #feefd4;
    --gold: #866a3d;
    --gold-soft: #a48852;
    --mark: #c9ad78;
  }
  * { margin: 0; padding: 0; box-sizing: border-box; }
  html, body {
    width: 1200px; height: 1000px; overflow: hidden;
    background: var(--page);
    font-family: "Cagliostro", sans-serif;
    color: var(--gold);
  }
  .canvas { position: relative; width: 1200px; height: 1000px; }
  .card {
    position: absolute; left: 211px; width: 773px; height: 426px;
    background: var(--card); overflow: hidden;
  }
  .card--front { top: 34px; }
  .card--back { top: 496px; }

  .brand { position: absolute; text-align: center; color: var(--gold); }
  .brand__circle { display: block; margin: 0 auto; border-radius: 50%; background: var(--mark); }
  .brand__name { font-family: "Cagliostro", sans-serif; line-height: 1.05; }

  .card--front .brand { left: 0; right: 0; top: 70px; }
  .card--front .brand__circle { width: 150px; height: 150px; }
  .card--front .brand__name { font-size: 42px; margin-top: 44px; }

  .card--back .brand { left: 40px; width: 230px; top: 98px; }
  .card--back .brand__circle { width: 110px; height: 110px; }
  .card--back .brand__name { font-size: 30px; margin-top: 34px; }

  .person { position: absolute; right: 10px; top: 12px; text-align: right; }
  .person__name { font-size: 45px; line-height: 1.1; color: var(--gold); }
  .person__title { font-size: 18px; color: var(--gold-soft); margin-top: 0; margin-right: 2px; }

  .contacts { position: absolute; right: 24px; top: 228px; list-style: none; }
  .contacts__item {
    display: flex; align-items: center; justify-content: flex-end;
    height: 46px; color: var(--gold);
  }
  .contacts__text { font-size: 15px; margin-right: 34px; }
  .contacts__item--email .contacts__text { font-size: 18px; }
  .contacts__item--address .contacts__text { font-size: 13.5px; }
  .contacts__icon { width: 24px; height: 26px; fill: none; stroke: var(--gold-soft); stroke-width: 1.6; }
  .contacts__icon--solid { fill: var(--gold-soft); stroke: none; }
</style>
</head>
<body>
<div class="canvas">

  <section class="card card--front" aria-label="Card front">
    <div class="brand">
      <span class="brand__circle"></span>
      <p class="brand__name">Birchwood Dwellworks, LLC</p>
    </div>
  </section>

  <section class="card card--back" aria-label="Card back">
    <div class="brand">
      <span class="brand__circle"></span>
      <p class="brand__name">Birchwood<br>Dwellworks, LLC</p>
    </div>

    <div class="person">
      <h1 class="person__name">Marla Pettigrew</h1>
      <p class="person__title">Director of Operations</p>
    </div>

    <ul class="contacts">
      <li class="contacts__item">
        <span class="contacts__text">(865)690-8142</span>
        <svg class="contacts__icon" viewBox="0 0 24 26" aria-hidden="true">
          <circle cx="12" cy="9" r="6"/>
          <path d="M2 24 C3 17 8 15 12 15 C16 15 21 17 22 24 Z"/>
        </svg>
      </li>
      <li class="contacts__item">
        <span class="contacts__text">(865)413-2958</span>
        <svg class="contacts__icon contacts__icon--solid" viewBox="0 0 24 26" aria-hidden="true">
          <path d="M9 3 L13 3 L12 9 L10 10 C10 14 11 17 13 19 L15 18 L18 22 L15 25 C9 23 6 14 7 5 Z"/>
        </svg>
      </li>
      <li class="contacts__item contacts__item--email">
        <span class="contacts__text">marla@birchwooddwellworks.example</span>
        <svg class="contacts__icon" viewBox="0 0 24 26" aria-hidden="true">
          <circle cx="12" cy="13" r="4"/>
          <path d="M16 9 L16 15 C16 18 21 18 21 13 C21 7 17 4 12 4 C7 4 3 8 3 13 C3 19 8 22 13 22 C15 22 17 21 18 20"/>
        </svg>
      </li>
      <li class="contacts__item contacts__item--address">
        <span class="contacts__text">20815 Thornbury Lane &nbsp;|Suite 300 Knoxville, TN 37091</span>
        <svg class="contacts__icon contacts__icon--solid" viewBox="0 0 24 26" aria-hidden="true">
          <path d="M12 1 C7 1 4 5 4 9 C4 15 12 25 12 25 C12 25 20 15 20 9 C20 5 17 1 12 1 Z M12 6 A3 3 0 1 1 12 12 A3 3 0 1 1 12 6 Z" fill-rule="evenodd"/>
        </svg>
      </li>
    </ul>
  </section>

</div>
</body>
</html>
```